Website Design Project for Beauty & Wellness Professionals

As background information, I have a website that is focused on Beauty & Wellness Professionals:
- Job Search (www.trilhavelora.com)
- Business Classifieds (negocios.trilhavelora.com)
- Freelancer Classifieds (freelancer.trilhavelora.com)
- Course Reviews (cursos.trilhavelora.com)

All those websites use standard templates.

I need a DESIGN for the HOME PAGE (no coding) of the Website Platform that consolidates the four platforms under the same design.

Website designs that we like:
- nestorly.com
- workpane.com

Target Market(s)

Brazilian Professionals from Beauty & Wellness sector

Industry/Entity Type

Business

Requirements
Must have
• Website designs that we like:
- nestorly.com
- workpane.com

```html
<!DOCTYPE html>
<html lang="en">
<head>
<meta charset="utf-8">
<title>Trilha Velora – Beauty &amp; Wellness Jobs</title>
<link rel="stylesheet" href="https://fonts.googleapis.com/css2?family=Arimo:wght@400;700&family=Oswald:wght@500;700&display=swap">
<style>
:root{
  --teal:#3aa7c9;
  --teal-dark:#1a6f96;
  --link:#1b6fa6;
  --green:#3cbf9b;
  --green-text:#1f9a6a;
  --orange:#ee6522;
  --gold:#fbbd1d;
  --gold-dark:#f3a70f;
  --ink:#333;
  --muted:#555;
  --line:#dcdcdc;
  --card-blue:#ebf8fc;
  --card-blue-line:#a6d9e6;
  --footer:#f1f1f1;
  --field:#e6e6e6;
}
*{box-sizing:border-box;margin:0;padding:0}
html,body{width:1200px;height:2410px;overflow:hidden}
body{position:relative;background:#fff;font-family:"Arimo",Arial,sans-serif;color:var(--ink)}
a{color:inherit;text-decoration:none}
.abs{position:absolute}

/* header */
.site-header{position:absolute;left:0;top:0;width:1200px;height:84px;background:#fff}
.brand{left:22px;top:20px;display:flex;align-items:center;gap:10px}
.brand-dot{width:40px;height:40px;border-radius:50%;background:var(--teal)}
.brand-name{font-size:30px;color:var(--teal-dark);font-weight:400}
.main-nav{left:284px;top:24px;display:flex;gap:7px}
.main-nav a{display:block;height:32px;line-height:32px;padding:0 17px;background:var(--teal);color:#fff;border-radius:10px;font-size:16px}
.account{top:37px;font-size:13px;font-weight:700;color:var(--green-text)}
.btn-advertise{left:993px;top:21px;width:186px;height:42px;border-radius:8px;background:linear-gradient(#ffd23f,var(--gold-dark));color:#6b3d00;font-size:20px;text-align:center;line-height:42px;border:1px solid #e39b08}

/* hero */
.hero{left:0;top:84px;width:1200px;height:510px;background:radial-gradient(ellipse at 50% 80%,#d99a4c 0%,#b8793a 25%,#7e9e4e 55%,#9fc36a 80%,#c9d8a0 100%)}
.hero-title{left:0;top:140px;width:1200px;text-align:center;font-family:"Oswald",sans-serif;font-weight:700;font-size:58px;line-height:70px;color:#fff;letter-spacing:-0.5px;text-shadow:-2px -2px 0 #2d8a3a,2px -2px 0 #2d8a3a,-2px 2px 0 #2d8a3a,2px 2px 0 #2d8a3a}
.search-bar{left:100px;top:353px;width:1002px;height:73px;background:rgba(40,40,40,.85);border-radius:8px}
.search-bar .field{position:absolute;top:14px;height:44px;background:#fff;border-radius:5px;font-size:20px;color:#666;line-height:44px;padding-left:16px}
.search-btn{position:absolute;left:822px;top:14px;width:166px;height:44px;border-radius:5px;background:linear-gradient(#ffd23f,var(--gold-dark));font-size:20px;color:#5a3600;text-align:center;line-height:44px}

/* tabs */
.tabs{left:8px;top:605px;display:flex;gap:10px}
.tab{width:176px;height:43px;border:1px solid #ccc;border-bottom:none;border-radius:8px 8px 0 0;background:#e9e9e9;font-size:14px;text-align:center;line-height:43px;color:#333}
.tab.active{background:#fff}

/* job cards */
.job-card{position:absolute;left:8px;width:774px;height:166px;border:1px solid var(--line);border-radius:10px;background:#fff}
.job-card.featured{background:var(--card-blue);border-color:var(--card-blue-line)}
.job-thumb{position:absolute;left:21px;top:18px;width:116px;height:97px;background:#fff;border:1px solid #ccc;display:flex;align-items:center;justify-content:center}
.job-thumb span{width:56px;height:56px;border-radius:50%;background:#7fc4c9}
.job-title{position:absolute;left:149px;top:17px;font-size:17px;color:var(--link)}
.job-desc{position:absolute;left:149px;top:46px;width:450px;font-size:13.5px;line-height:17px;color:#444}
.job-loc{position:absolute;left:149px;top:126px;font-size:13.5px;color:#333}
.job-loc b{font-weight:700}
.badge{position:absolute;right:14px;top:16px;height:27px;padding:0 13px;line-height:27px;color:#fff;font-size:14.5px;border-radius:2px 0 0 2px}
.badge.autonomous{background:var(--green)}
.badge.clt{background:var(--orange)}
.job-date{position:absolute;right:56px;top:53px;font-size:12px;color:var(--green-text)}
.job-icon{position:absolute;right:18px;top:51px}
.see-all{left:16px;top:2063px;font-size:14px;font-weight:700;color:var(--link)}

/* sidebar */
.ad-free{left:821px;top:605px;width:367px;height:169px;background:repeating-conic-gradient(from 0deg at 50% 100%,#86cf68 0 6deg,#9ad97d 6deg 12deg)}
.ad-free-title{position:absolute;top:10px;width:100%;text-align:center;font-family:"Oswald",sans-serif;font-weight:500;font-size:23px;line-height:30px;color:#fff;text-shadow:0 1px 2px rgba(0,0,0,.3)}
.ad-free-btn{position:absolute;left:63px;top:97px;width:243px;height:52px;border-radius:8px;background:linear-gradient(#ff9540,#ec5b10);color:#fff;font-size:21px;text-align:center;line-height:52px}
.ad-promo{left:821px;top:789px;width:367px;height:306px;background:#3d3d3d;overflow:hidden}
.ad-promo-brand{position:absolute;left:100px;top:12px;display:flex;align-items:center;gap:10px;color:#fff;font-size:23px}
.ad-promo-brand i{width:24px;height:24px;border-radius:50%;background:#fff;display:block}
.ad-promo-text{position:absolute;left:0;top:70px;width:100%;text-align:center;color:#fff;font-weight:700;font-size:19px;line-height:26px;white-space:nowrap;z-index:2}
.ad-promo-shirt{position:absolute;left:90px;top:140px;width:190px;height:150px;background:radial-gradient(#2a2a2a,#151515);border-radius:30px 30px 4px 4px;z-index:1}
.ad-promo-btn{position:absolute;left:109px;top:253px;width:152px;height:38px;background:#1aa3a8;color:#fff;font-weight:700;font-size:17px;text-align:center;line-height:38px;z-index:2}
.ad-choice{position:absolute;right:4px;top:3px;width:12px;height:12px;background:#7ec3e6}

.side-heading{font-size:19px;font-weight:700;color:#222;padding-bottom:6px;border-bottom:1px solid var(--line);width:369px}
.connections{left:821px;top:1180px;font-size:14px;color:#333;width:360px;line-height:20px}
.connections .fb{display:inline-block;width:14px;height:14px;background:#3b5998;vertical-align:-2px;margin-right:4px}
.connections a{color:var(--link)}
.friends{left:821px;top:1225px;display:flex;gap:4px}
.friends span{width:50px;height:60px;background:linear-gradient(135deg,#8e9aa8,#5a6470)}
.uncover{left:821px;top:1290px;font-size:14px;font-weight:700;color:var(--link)}

.vacancies{left:821px;top:1365px;width:369px;list-style:none}
.vacancies li{height:33.3px;line-height:33px;border-bottom:1px solid #ececec;font-size:14.5px;color:#444;padding-left:2px}
.vacancies li::before{content:"› ";color:#666}

/* footer */
.site-footer{left:0;top:2133px;width:1200px;height:277px;background:var(--footer)}
.foot-col{position:absolute;top:42px}
.foot-col h3{font-size:19px;font-weight:700;color:#333;margin-bottom:14px}
.foot-col ul{list-style:none;font-size:14px;line-height:17.5px;color:#333}
.foot-field{position:absolute;height:42px;width:268px;background:var(--field);border:1px solid #d2d2d2;border-radius:6px;font-size:13px;color:#555;line-height:42px;padding-left:14px}
.foot-search{position:absolute;left:135px;top:152px;width:128px;height:44px;border-radius:6px;background:#8c8c8c;color:#fff;font-size:14px;text-align:center;line-height:44px}
.social{display:flex;gap:10px;margin-bottom:12px}
.social span{width:36px;height:36px;border-radius:50%;background:#777}
.news-text{font-size:12.5px;line-height:16px;color:#333;width:240px}
.news-field{margin-top:12px;width:226px;height:33px;border-radius:17px;background:#8c8c8c;color:#fff;font-size:12.5px;line-height:33px;padding-left:18px}
.news-link{margin-top:14px;font-size:12.5px;font-weight:700;color:#333}
</style>
</head>
<body>

<header class="site-header">
  <div class="abs brand"><span class="brand-dot"></span><span class="brand-name">Trilha Velora</span></div>
  <nav class="abs main-nav">
    <a href="#">Home</a><a href="#">Professionals</a><a href="#">Business</a><a href="#">Partners</a><a href="#">Blog</a>
  </nav>
  <a class="abs account" style="left:830px" href="#">SIGN UP</a>
  <a class="abs account" style="left:907px" href="#">LOG IN</a>
  <a class="abs btn-advertise" href="#">Advertise Now!</a>
</header>

<section class="abs hero" role="img" aria-label="Photo of a beauty salon interior with tan leather styling chairs and green walls"></section>
<h1 class="abs hero-title">Espaco para Empresas e Profissionais de<br>Beleza, Estetita e Bem-estar</h1>
<form class="abs search-bar">
  <div class="field" style="left:12px;width:172px">Hairdresser
    <svg style="position:absolute;right:12px;top:18px" width="14" height="9" viewBox="0 0 14 9"><path d="M0 0h14L7 9z" fill="#555"/></svg>
  </div>
  <div class="field" style="left:196px;width:209px">Location</div>
  <div class="field" style="left:417px;width:393px">Job Title, Keyworkds or Company</div>
  <div class="search-btn">Search</div>
</form>

<div class="abs tabs">
  <div class="tab active">Featured Jobs</div>
  <div class="tab">Latest Jobs</div>
  <div class="tab">Jobs by Profession</div>
</div>

<article class="job-card featured" style="top:660px">
  <div class="job-thumb"><span></span></div>
  <a class="job-title" href="#">Manicure and Pedicure - Vila Mariana - São Paulo (SP)</a>
  <p class="job-desc">Location easy access, close to metro Santa Cruz. Hours of work: 6 hours work from Monday to Saturday. Experience Minimum of 1 year with courses and diplomas. Being communicative ... Location: Rua Coronel Alvarim - Mariana VL - SP</p>
  <p class="job-loc"><b>Location:</b> Rua Coronel Alvarim - Mariana VL - SP</p>
  <span class="badge autonomous">Autonomous</span>
  <span class="job-date">Jul 31, 2013</span>
  <svg class="job-icon" width="20" height="18" viewBox="0 0 20 18"><rect x="1" y="1" width="18" height="14" fill="#fff" stroke="#3a76b8"/><rect x="3" y="4" width="14" height="2" fill="#3a76b8"/><rect x="3" y="8" width="9" height="2" fill="#f0b43c"/></svg>
</article>
<article class="job-card" style="top:834px">
  <div class="job-thumb"><span></span></div>
  <a class="job-title" href="#">Aux. Hairdresser (Escovista) - Santo André (SP)</a>
  <p class="job-desc">We are in the process of expanding our workforce and we aim to identify people with "solid technical skills and quality + fast + easy r ...</p>
  <p class="job-loc"><b>Location:</b> Rua Coronel Alvarim - Mariana VL - SP</p>
  <span class="badge clt">Registered (CLT)</span>
  <span class="job-date">Jul 31, 2013</span>
  <svg class="job-icon" width="20" height="18" viewBox="0 0 20 18"><rect x="1" y="1" width="18" height="14" fill="#fff" stroke="#3a76b8"/><rect x="3" y="4" width="14" height="2" fill="#3a76b8"/><rect x="3" y="8" width="9" height="2" fill="#f0b43c"/></svg>
</article>
<article class="job-card featured" style="top:1008px">
  <div class="job-thumb"><span></span></div>
  <a class="job-title" href="#">Manicure and Pedicure - Vila Mariana - São Paulo (SP)</a>
  <p class="job-desc">Location easy access, close to metro Santa Cruz. Hours of work: 6 hours work from Monday to Saturday. Experience Minimum of 1 year with courses and diplomas. Being communicative ... Location: Rua Coronel Alvarim - Mariana VL - SP</p>
  <p class="job-loc"><b>Location:</b> Rua Coronel Alvarim - Mariana VL - SP</p>
  <span class="badge autonomous">Autonomous</span>
  <span class="job-date">Jul 31, 2013</span>
  <svg class="job-icon" width="20" height="18" viewBox="0 0 20 18"><rect x="1" y="1" width="18" height="14" fill="#fff" stroke="#3a76b8"/><rect x="3" y="4" width="14" height="2" fill="#3a76b8"/><rect x="3" y="8" width="9" height="2" fill="#f0b43c"/></svg>
</article>
<article class="job-card" style="top:1182px">
  <div class="job-thumb"><span></span></div>
  <a class="job-title" href="#">Aux. Hairdresser (Escovista) - Santo André (SP)</a>
  <p class="job-desc">We are in the process of expanding our workforce and we aim to identify people with "solid technical skills and quality + fast + easy r ...</p>
  <p class="job-loc"><b>Location:</b> Rua Coronel Alvarim - Mariana VL - SP</p>
  <span class="badge clt">Registered (CLT)</span>
  <span class="job-date">Jul 31, 2013</span>
  <svg class="job-icon" width="20" height="18" viewBox="0 0 20 18"><rect x="1" y="1" width="18" height="14" fill="#fff" stroke="#3a76b8"/><rect x="3" y="4" width="14" height="2" fill="#3a76b8"/><rect x="3" y="8" width="9" height="2" fill="#f0b43c"/></svg>
</article>
<article class="job-card featured" style="top:1356px">
  <div class="job-thumb"><span></span></div>
  <a class="job-title" href="#">Manicure and Pedicure - Vila Mariana - São Paulo (SP)</a>
  <p class="job-desc">Location easy access, close to metro Santa Cruz. Hours of work: 6 hours work from Monday to Saturday. Experience Minimum of 1 year with courses and diplomas. Being communicative ... Location: Rua Coronel Alvarim - Mariana VL - SP</p>
  <p class="job-loc"><b>Location:</b> Rua Coronel Alvarim - Mariana VL - SP</p>
  <span class="badge autonomous">Autonomous</span>
  <span class="job-date">Jul 31, 2013</span>
  <svg class="job-icon" width="20" height="18" viewBox="0 0 20 18"><rect x="1" y="1" width="18" height="14" fill="#fff" stroke="#3a76b8"/><rect x="3" y="4" width="14" height="2" fill="#3a76b8"/><rect x="3" y="8" width="9" height="2" fill="#f0b43c"/></svg>
</article>
<article class="job-card" style="top:1530px">
  <div class="job-thumb"><span></span></div>
  <a class="job-title" href="#">Aux. Hairdresser (Escovista) - Santo André (SP)</a>
  <p class="job-desc">We are in the process of expanding our workforce and we aim to identify people with "solid technical skills and quality + fast + easy r ...</p>
  <p class="job-loc"><b>Location:</b> Rua Coronel Alvarim - Mariana VL - SP</p>
  <span class="badge clt">Registered (CLT)</span>
  <span class="job-date">Jul 31, 2013</span>
  <svg class="job-icon" width="20" height="18" viewBox="0 0 20 18"><rect x="1" y="1" width="18" height="14" fill="#fff" stroke="#3a76b8"/><rect x="3" y="4" width="14" height="2" fill="#3a76b8"/><rect x="3" y="8" width="9" height="2" fill="#f0b43c"/></svg>
</article>
<article class="job-card featured" style="top:1704px">
  <div class="job-thumb"><span></span></div>
  <a class="job-title" href="#">Manicure and Pedicure - Vila Mariana - São Paulo (SP)</a>
  <p class="job-desc">Location easy access, close to metro Santa Cruz. Hours of work: 6 hours work from Monday to Saturday. Experience Minimum of 1 year with courses and diplomas. Being communicative ... Location: Rua Coronel Alvarim - Mariana VL - SP</p>
  <p class="job-loc"><b>Location:</b> Rua Coronel Alvarim - Mariana VL - SP</p>
  <span class="badge autonomous">Autonomous</span>
  <span class="job-date">Jul 31, 2013</span>
  <svg class="job-icon" width="20" height="18" viewBox="0 0 20 18"><rect x="1" y="1" width="18" height="14" fill="#fff" stroke="#3a76b8"/><rect x="3" y="4" width="14" height="2" fill="#3a76b8"/><rect x="3" y="8" width="9" height="2" fill="#f0b43c"/></svg>
</article>
<article class="job-card" style="top:1878px">
  <div class="job-thumb"><span></span></div>
  <a class="job-title" href="#">Aux. Hairdresser (Escovista) - Santo André (SP)</a>
  <p class="job-desc">We are in the process of expanding our workforce and we aim to identify people with "solid technical skills and quality + fast + easy r ...</p>
  <p class="job-loc"><b>Location:</b> Rua Coronel Alvarim - Mariana VL - SP</p>
  <span class="badge clt">Registered (CLT)</span>
  <span class="job-date">Jul 31, 2013</span>
  <svg class="job-icon" width="20" height="18" viewBox="0 0 20 18"><rect x="1" y="1" width="18" height="14" fill="#fff" stroke="#3a76b8"/><rect x="3" y="4" width="14" height="2" fill="#3a76b8"/><rect x="3" y="8" width="9" height="2" fill="#f0b43c"/></svg>
</article>

<a class="abs see-all" href="#">See All Featured Jobs &nbsp;<svg width="10" height="10" viewBox="0 0 10 10"><path d="M1 0l8 5-8 5z" fill="#1b6fa6"/></svg></a>

<aside class="abs ad-free">
  <div class="ad-free-title">Owners Salons, Spas and Clinics<br>Advertise Your Job Vacancy (FREE)!</div>
  <div class="ad-free-btn">Advertise Now!</div>
</aside>
<aside class="abs ad-promo">
  <span class="ad-choice"></span>
  <div class="ad-promo-brand"><i></i>Lumen Metrics</div>
  <div class="ad-promo-text">Lumen Metrics &amp; Forgeboard teamed<br>up to offer this custom shirt!</div>
  <div class="ad-promo-shirt" role="img" aria-label="Black promotional t-shirt with a printed emblem"></div>
  <div class="ad-promo-btn">Get it now</div>
</aside>

<h2 class="abs side-heading" style="left:821px;top:1130px">Inside Connections</h2>
<p class="abs connections"><span class="fb"></span><a href="#">Marta Quevedo</a>, <a href="#">Lina Sorvetti</a> and 24 other friends use <a href="#">Workpane</a>.</p>
<div class="abs friends" role="img" aria-label="Row of friend profile photos"><span></span><span></span><span></span><span></span><span></span><span></span></div>
<a class="abs uncover" href="#">Uncover Inside Connections</a>

<h2 class="abs side-heading" style="left:821px;top:1333px">Job Vacancies</h2>
<ul class="abs vacancies">
  <li>Assistant Hairdresser (39)</li>
  <li>Assistant Cleaning (5)</li>
  <li>Hairdresser (125)</li>
  <li>Epilator (28)</li>
  <li>Designer Eyebrow (11)</li>
  <li>Featured (24)</li>
  <li>Nurse (2)</li>
  <li>Esthetician (60)</li>
  <li>Physiotherapist (9)</li>
  <li>Management / Coordination (17)</li>
  <li>Manicure and Pedicure (256)</li>
  <li>Makeup artist (8)</li>
  <li>Practitioner (22)</li>
  <li>Other (15)</li>
  <li>Podiatrist (13)</li>
  <li>Reception / Customer Service (35)</li>
  <li>Sales Cosmetics (22)</li>
</ul>

<footer class="abs site-footer">
  <div class="foot-col" style="left:22px">
    <h3>Main Navigation</h3>
    <ul><li>Home</li><li>About Us</li><li>Professionals</li><li>Business</li><li>Partners</li><li>Blog</li><li>Contact Us</li></ul>
  </div>
  <div class="foot-col" style="left:299px">
    <h3>Job Categories</h3>
    <ul><li>Hairdresser</li><li>Beautician</li><li>Manicure</li><li>Massage therapist</li><li>Epilator</li><li>Reception</li><li>Sales</li></ul>
  </div>
  <div class="foot-col" style="left:543px;width:280px;height:230px">
    <h3>Search for your job!</h3>
    <div class="foot-field" style="left:0;top:54px">Digite aqui a vaga que voce procura!</div>
    <div class="foot-field" style="left:0;top:103px">Localizacao</div>
    <div class="foot-field" style="left:0;top:152px;width:120px">1 km
      <svg style="position:absolute;right:10px;top:16px" width="22" height="10" viewBox="0 0 22 10"><rect x="0" y="-4" width="1" height="18" fill="#999"/><path d="M9 2h10l-5 6z" fill="#666"/></svg>
    </div>
    <div class="foot-search">search</div>
  </div>
  <div class="foot-col" style="left:928px">
    <h3>Connect With Us</h3>
    <div class="social"><span></span><span></span><span></span><span></span><span></span></div>
    <p class="news-text">subscribe to our monthly newsletter and get the best deals and discounts</p>
    <div class="news-field">enter email address</div>
    <p class="news-link">subscribe now &nbsp;<svg width="10" height="10" viewBox="0 0 10 10"><path d="M1 1l8 4-8 4z" fill="#333"/></svg></p>
  </div>
</footer>

</body>
</html>
```